owlbrass website

commerce website to sell cookeries, brackets, mailboxes and to show off homes built. Modern Steel in design see tandra wheels web page to be like: https://www.tandrawheels.example/en/ sorry its net haven hosting word press divi

must be able to add products to page

Target Market(s)

mainly western states of U.S.

Industry/Entity Type

Building Product

Coding

Coded - Design and coding required

Number of Pages Required

3 page

Font styles to use
Sans Serif

Colors

Designer to choose colors to be used in the design.

Requirements
Must have
• customers to be able to order products from page
• net haven hosting word press divi

```html
<!DOCTYPE html>
<html lang="en">
<head>
<meta charset="utf-8">
<title>Owl Brass – Steel Products &amp; Homes Built</title>
<link href="https://fonts.googleapis.com/css2?family=Montserrat:ital,wght@0,300;0,400;0,500;0,600;0,700;0,800;1,400&display=swap" rel="stylesheet">
<style>
:root{
  --brand:#4a5d8a;
  --brand-dark:#42547e;
  --ink:#111111;
  --text:#3a3a3a;
  --muted:#555555;
  --header-dark:#1c1c1c;
  --paper:#ffffff;
  --section-grey:#f2f2f2;
  --rule:#d6d9e0;
}
*{box-sizing:border-box;margin:0;padding:0}
html,body{width:1200px;height:2346px;overflow:hidden}
body{position:relative;background:var(--paper);font-family:"Montserrat",sans-serif;color:var(--text)}
.abs{position:absolute}

/* header */
.site-header{position:absolute;left:0;top:0;width:1200px;height:91px;background:var(--paper);z-index:2}
.brand-plate{position:absolute;left:0;top:0;width:360px;height:106px;background:var(--header-dark);clip-path:polygon(0 0,100% 0,88% 100%,0 100%);z-index:3}
.brand-plate .wordmark{position:absolute;left:0;width:320px;top:58px;text-align:center;color:#fff;font-size:25px;font-weight:500;letter-spacing:.5px}
.brand-plate .mark{position:absolute;left:145px;top:14px;width:30px;height:30px;border-radius:50%;background:#fff}
.main-nav{position:absolute;top:38px;font-size:12.5px;letter-spacing:.4px;color:#444}
.main-nav span{position:absolute;white-space:nowrap}
.main-nav .active{color:var(--brand);font-weight:600}
.nav-sep{position:absolute;left:945px;top:36px;width:1px;height:20px;background:#ddd}
.nav-icon{position:absolute;top:36px;width:18px;height:18px}

/* hero */
.hero{position:absolute;left:0;top:91px;width:1200px;height:509px;
  background:linear-gradient(180deg,#c9c4cf 0%,#b9b8c0 25%,#8f9290 50%,#4e5b3d 72%,#3a4636 100%)}
.hero-title{position:absolute;left:0;width:1200px;top:450px;text-align:center;color:#fff;font-size:32px;font-weight:700;line-height:45px;letter-spacing:.6px;text-shadow:0 2px 6px rgba(0,0,0,.35)}
.scroll-mouse{position:absolute;left:592px;top:547px;width:16px;height:27px;border:1.5px solid #fff;border-radius:8px}
.scroll-mouse::after{content:"";position:absolute;left:6px;top:5px;width:1.5px;height:6px;background:#fff}

/* section heading */
.section-title{position:absolute;left:0;width:1200px;text-align:center;font-size:33px;color:var(--ink);font-weight:300;letter-spacing:.5px}
.section-title b{font-weight:800}
.divider{position:absolute;height:12px}
.divider::before{content:"";position:absolute;left:0;right:0;top:5.5px;height:1px;background:var(--rule)}
.divider i{position:absolute;top:1px;width:18px;height:10px;background:var(--brand)}

/* products */
.product-card{position:absolute;top:754px;width:293px;height:233px;border-radius:0 40px 0 40px;overflow:hidden}
.product-card .label{position:absolute;left:0;right:0;bottom:18px;text-align:center;color:#fff;font-size:35px;font-weight:800;letter-spacing:.5px;text-shadow:0 2px 5px rgba(0,0,0,.6)}
.product-card .shade{position:absolute;left:0;right:0;bottom:0;height:110px;background:linear-gradient(180deg,rgba(0,0,0,0),rgba(0,0,0,.75))}
.photo-cookery{background:linear-gradient(160deg,#a09a92,#48463f 55%,#2a2824)}
.photo-brackets{background:linear-gradient(150deg,#6d7e80,#4b5a5c 50%,#2f3434)}
.photo-mailbox{background:linear-gradient(160deg,#c8a67e,#b9bcc0 45%,#7f8a6a)}

/* about */
.about{position:absolute;left:0;top:1057px;width:1200px;height:466px;background:var(--section-grey)}
.about-title{position:absolute;left:141px;top:1121px;font-size:33px;color:var(--ink);font-weight:300}
.about-title b{font-weight:800}
.about-lead{position:absolute;left:142px;top:1195px;width:460px;font-size:13.6px;font-weight:700;line-height:23px;color:#222}
.about-body{position:absolute;left:142px;top:1249px;width:460px;font-size:12.4px;line-height:20.3px;color:var(--muted)}
.btn-read{position:absolute;left:141px;top:1409px;width:134px;height:37px;border-radius:19px;background:var(--brand);color:#fff;font-size:12.5px;font-weight:600;text-align:center;line-height:37px;letter-spacing:.4px}
.about-frame{position:absolute;left:654px;top:1133px;width:399px;height:313px;border:1.5px solid var(--brand)}
.about-photo{position:absolute;left:663px;top:1129px;width:396px;height:309px;background:linear-gradient(170deg,#8fb0d6 0%,#c5d2df 30%,#5e6d52 55%,#a8a196 80%,#cbbd9f 100%)}

/* reviews */
.avatar{position:absolute;left:565px;top:1691px;width:70px;height:70px;border-radius:50%;border:2px solid var(--brand);padding:3px;background:#fff}
.avatar span{display:block;width:100%;height:100%;border-radius:50%;background:linear-gradient(180deg,#8a7a6e,#c2a38b)}
.quote-mark{position:absolute;left:530px;top:1760px;font-size:190px;font-weight:300;font-style:italic;color:#eeeeee;line-height:1}
.quote{position:absolute;left:240px;width:720px;top:1792px;text-align:center;font-style:italic;font-size:13.8px;line-height:25.5px;color:#444}
.quote-author{position:absolute;left:0;width:1200px;top:1885px;text-align:center;font-size:15.5px;font-weight:500;color:#111}
.dots{position:absolute;left:574px;top:1930px;display:flex;gap:6px}
.dots span{width:8px;height:8px;border-radius:50%;border:1px solid var(--brand)}
.dots span.on{background:var(--brand)}
.arrow{position:absolute;top:1786px}

/* footer */
.site-footer{position:absolute;left:0;top:2051px;width:1200px;height:295px;background:var(--brand)}
.footer-mark{position:absolute;left:578px;top:2012px;width:44px;height:44px;border-radius:50%;background:#fff}
.footer-wordmark{position:absolute;left:0;width:1200px;top:2082px;text-align:center;color:#fff;font-size:31px;font-weight:500;letter-spacing:.5px}
.footer-nav{position:absolute;left:0;width:1200px;top:2151px;text-align:center;color:#fff;font-size:12.8px;letter-spacing:.3px}
.footer-nav span{margin:0 16px}
.footer-nav .active{font-weight:700}
.footer-nav .sep{margin:0 14px}
.footer-rule{position:absolute;left:0;width:1200px;height:1px;background:rgba(255,255,255,.14)}
.contact{position:absolute;top:2229px;color:#fff}
.contact .ico{position:absolute;left:0;top:0;width:39px;height:39px;border:2px solid #fff;border-radius:50%}
.contact .ico svg{position:absolute;left:9px;top:9px}
.contact .k{position:absolute;left:50px;top:3px;font-size:12px;font-weight:600;letter-spacing:.4px;white-space:nowrap}
.contact .v{position:absolute;left:50px;top:20px;font-size:13px;white-space:nowrap}
.contact .v.big{font-size:17px;font-weight:600;top:18px}
.contact .v.mid{font-size:14px;font-weight:600}
.vrule{position:absolute;top:2228px;width:1px;height:40px;background:rgba(255,255,255,.3)}
.copyright{position:absolute;left:141px;top:2313px;color:#fff;font-size:12.4px}
.social{position:absolute;top:2306px;width:28px;height:28px;border:1.3px solid #fff;border-radius:50%}
</style>
</head>
<body>

<header class="site-header">
  <nav class="main-nav">
    <span class="active" style="left:435px">HOME</span>
    <span style="left:517px">PRODUCTS</span>
    <span style="left:632px">HOMES BUILT</span>
    <span style="left:764px">ABOUT</span>
    <span style="left:852px">CONTACT</span>
  </nav>
  <div class="nav-sep"></div>
  <svg class="nav-icon" style="left:968px" viewBox="0 0 18 18" fill="none" stroke="#4a5d8a" stroke-width="1.4"><circle cx="9" cy="6" r="3.5"/><path d="M2.5 16.5c0-3.6 2.9-5.5 6.5-5.5s6.5 1.9 6.5 5.5z"/></svg>
  <svg class="nav-icon" style="left:1004px" viewBox="0 0 18 18" fill="none" stroke="#4a5d8a" stroke-width="1.5"><circle cx="7.5" cy="7.5" r="5.5"/><path d="M11.5 11.5l5 5"/></svg>
  <svg class="nav-icon" style="left:1041px" viewBox="0 0 18 18" fill="none" stroke="#4a5d8a" stroke-width="1.4"><path d="M1 2h3l2 9h9l2-7H5"/><circle cx="7" cy="15" r="1.3"/><circle cx="14" cy="15" r="1.3"/></svg>
</header>
<div class="brand-plate">
  <div class="mark"></div>
  <div class="wordmark">OWL BRASS</div>
</div>

<section class="hero" role="img" aria-label="Modern white house with dark grey garage and slatted steel fence on a green lawn">
</section>
<h1 class="hero-title abs">WE SELL COOKERIES, BRACKETS, MAILBOXES<br>AND TO SHOW OFF HOMES BUILT.</h1>
<div class="scroll-mouse"></div>

<h2 class="section-title" style="top:661px">OUR <b>PRODUCT</b></h2>
<div class="divider" style="left:517px;top:714px;width:166px"><i style="left:74px"></i></div>

<a class="product-card" style="left:141px">
  <div class="photo-cookery abs" style="inset:0" role="img" aria-label="Hexagonal steel fire pit cookery in a workshop"></div>
  <div class="shade"></div><span class="label">Cookeries</span>
</a>
<a class="product-card" style="left:454px">
  <div class="photo-brackets abs" style="inset:0" role="img" aria-label="Stack of square steel tube brackets"></div>
  <div class="shade"></div><span class="label">Brackets</span>
</a>
<a class="product-card" style="left:766px">
  <div class="photo-mailbox abs" style="inset:0" role="img" aria-label="Silver mailbox with red flag receiving a newspaper"></div>
  <div class="shade"></div><span class="label">Mailboxes</span>
</a>

<section class="about"></section>
<h2 class="about-title">ABOUT <b>OWL BRASS</b></h2>
<div class="divider" style="left:141px;top:1172px;width:94px"><i style="left:0"></i></div>
<p class="about-lead">Ut wisi enim ad minim veniam, quis nostrud exercmli tationmol ullamcor per suscipit lobortis nisl ut.</p>
<p class="about-body">Lorem ipsum dolor sit amet, consectetuer adipiscing elit, sed diam non ummy nibh euismod tincidunt ut laoreet dolore magna aliquam eratmo volutpat. Ut wisi enim ad minim veniam, quismod nostrud exerci tation ullamcorper suscipit lobortis nisl ut aliquip ex ea commodo consequat. Duis autem vel eum iriure dolor in hendrerit in &nbsp;at vero eros et accumki san et iusto odio dignissim qui blandit praesent luptatum zzril delenitn augue duis dolore te feugait nulla facilisi.</p>
<a class="btn-read">READ MORE</a>
<div class="about-frame"></div>
<div class="about-photo" role="img" aria-label="Contemporary concrete house with large glass windows under trees and blue sky"></div>

<h2 class="section-title" style="top:1586px">CUSTOMER <b>REVIEWS</b></h2>
<div class="divider" style="left:517px;top:1638px;width:166px"><i style="left:74px"></i></div>
<div class="avatar"><span role="img" aria-label="Customer portrait"></span></div>
<div class="quote-mark">&ldquo;</div>
<p class="quote">&ldquo;Duis autem vel eum iriure dolor in hendrerit in vulputate velit esse molestie consequat, vel illum dolore eu feugiat nulla et iusto odio dignissim qui blandit praesent luptatum zzril delenit augue duis dolore te feugait nulla facilisi.&rdquo;</p>
<p class="quote-author">- Marco &amp; Lena Varga</p>
<div class="dots"><span class="on"></span><span></span><span></span><span></span></div>
<svg class="arrow" style="left:141px" width="31" height="60" viewBox="0 0 31 60" fill="none" stroke="#4a5d8a" stroke-width="1"><path d="M30 0L1 30l29 30"/></svg>
<svg class="arrow" style="left:1028px" width="31" height="60" viewBox="0 0 31 60" fill="none" stroke="#4a5d8a" stroke-width="1"><path d="M1 0l29 30L1 60"/></svg>

<footer class="site-footer"></footer>
<div class="footer-mark"></div>
<div class="footer-wordmark">OWL BRASS</div>
<nav class="footer-nav">
  <span class="active">HOME</span><span class="sep">•</span><span>PRODUCTS</span><span class="sep">•</span><span>HOMES BUILT</span><span class="sep">•</span><span>ABOUT</span><span class="sep">•</span><span>CONTACT</span>
</nav>
<div class="footer-rule" style="top:2196px"></div>

<div class="contact" style="left:141px">
  <div class="ico"><svg width="17" height="17" viewBox="0 0 17 17" fill="none" stroke="#fff" stroke-width="1.6"><path d="M8.5 16s5.5-5.5 5.5-9.5a5.5 5.5 0 0 0-11 0C3 10.5 8.5 16 8.5 16z"/><circle cx="8.5" cy="6.5" r="1.8"/></svg></div>
  <div class="k">ADDRESS</div><div class="v">123, Loream Ipsum, AB-123 456</div>
</div>
<div class="vrule" style="left:464px"></div>
<div class="contact" style="left:541px">
  <div class="ico"><svg width="17" height="17" viewBox="0 0 17 17" fill="#fff"><path d="M3.6 1l2.6 3.1-1.5 1.8c.9 2 2.4 3.6 4.4 4.6l1.8-1.5 3.1 2.5-1.2 2.8C8.5 14.5 2.6 8.7 1 4.4z"/></svg></div>
  <div class="k">CALL</div><div class="v big">123 456 7890</div>
</div>
<div class="vrule" style="left:788px"></div>
<div class="contact" style="left:866px">
  <div class="ico"><svg width="17" height="17" viewBox="0 0 17 17" fill="#fff"><path d="M2 4h13v1L8.5 9 2 5z"/><path d="M2 6.5l6.5 4 6.5-4V13H2z"/></svg></div>
  <div class="k">EMAIL</div><div class="v mid">info@owlbrass.com</div>
</div>

<div class="footer-rule" style="top:2296px"></div>
<p class="copyright">Copyright 2020 Owl Brass Home Building Retail. All Rights Reserved.</p>
<span class="social" style="left:925px"></span>
<span class="social" style="left:961px"></span>
<span class="social" style="left:996px"></span>
<span class="social" style="left:1031px"></span>

</body>
</html>
```